Business Card Design Project

After recently finishing a design project for the company logo using quillnest, it's now time for a business card. Attached to this is the logo.

The requirements for the business card are pretty straightforward:

- A clean, uncomplicated look
- Consistent usage of fonts
- Designs for both single sided and double sided cards
- A modern layout with preferably space to refer to social media accounts and/or downloadable vcards through a qr code
- consistent application of the company colour scheme: red/white. Hex codes for exact colour can be provided

Thanks!

```html
<!DOCTYPE html>
<html lang="en">
<head>
<meta charset="utf-8">
<title>Kiln Row Recruiting – Business Card, Single Sided</title>
<link rel="stylesheet" href="https://fonts.googleapis.com/css2?family=Noto+Sans:wght@400&display=swap">
<style>
  :root {
    --brand-red: #e31e24;
    --ink: #231f20;
    --black: #000000;
    --white: #ffffff;
    --paper-tint: #f3f2f2;
    --text-font: "Noto Sans", Verdana, sans-serif;
  }
  * { margin: 0; padding: 0; box-sizing: border-box; }
  html, body {
    width: 1200px;
    height: 900px;
    overflow: hidden;
    background: var(--white);
    font-family: var(--text-font);
  }
  .stage { position: relative; width: 1200px; height: 900px; }

  .version-banner {
    position: absolute;
    left: 0; top: 38px;
    width: 1200px; height: 58px;
    background: var(--black);
    color: var(--white);
    font-size: 33px;
    letter-spacing: 3px;
    line-height: 58px;
    text-align: center;
  }

  .business-card {
    position: absolute;
    left: 75px; top: 171px;
    width: 1050px; height: 600px;
    background: var(--white);
    box-shadow: 0 4px 22px rgba(0, 0, 0, 0.55);
    overflow: hidden;
  }
  .card-texture {
    position: absolute; inset: 0;
    background: linear-gradient(135deg, var(--white) 0%, var(--paper-tint) 55%, var(--white) 100%);
  }
  .corner-wedge {
    position: absolute; left: 0; top: 0;
    width: 297px; height: 414px;
  }
  .brand-mark {
    position: absolute;
    left: 52px; top: 72px;
    width: 58px; height: 58px;
    background: var(--brand-red);
  }
  .brand-name {
    position: absolute;
    left: 0; top: 12px;
    width: 1050px;
    color: var(--ink);
    font-weight: 400;
    text-align: center;
  }
  .brand-name-main {
    display: block;
    font-size: 122px;
    line-height: 140px;
    letter-spacing: -2px;
    padding-left: 60px;
  }
  .brand-name-sub {
    display: block;
    font-size: 58px;
    line-height: 70px;
    letter-spacing: 0.42em;
    padding-left: 180px;
  }

  .contact-block {
    position: absolute;
    right: 45px; top: 306px;
    text-align: right;
    color: var(--black);
    white-space: nowrap;
  }
  .person-name {
    font-size: 58px;
    line-height: 70px;
    letter-spacing: 3px;
    color: var(--brand-red);
  }
  .person-role,
  .person-phone,
  .person-email {
    font-size: 32px;
    line-height: 36px;
    letter-spacing: 2px;
  }
  .person-role { margin-top: 14px; }
  .person-phone { margin-top: 30px; }
  .person-email { margin-top: 30px; }
</style>
</head>
<body>
  <main class="stage">
    <header class="version-banner">SINGLE SIDED VERSION</header>

    <section class="business-card">
      <div class="card-texture" role="img" aria-label="Faint light grey brick pattern across the card background"></div>

      <svg class="corner-wedge" viewBox="0 0 297 414" aria-hidden="true">
        <polygon points="0,0 297,0 0,414" fill="var(--black)"/>
      </svg>
      <span class="brand-mark" aria-hidden="true"></span>

      <h1 class="brand-name">
        <span class="brand-name-main">Kiln Row</span>
        <span class="brand-name-sub">RECRUITING</span>
      </h1>

      <address class="contact-block" style="font-style: normal;">
        <p class="person-name">JOHN DOE</p>
        <p class="person-role">RECRUITER</p>
        <p class="person-phone">123.456.7890</p>
        <p class="person-email">JOHN@KILNROW.COM</p>
      </address>
    </section>
  </main>
</body>
</html>
```